Bright Valley Centre - is state of the art audiology clinic and needs a business card design

the card should be oriented in 'portrait' mode and have a clinic logo. The card should be double sided, with logo on the front and my details on the other side of the card

We would also like to use a tagline of 'Experts in Hearing Care'

```html
<!DOCTYPE html>
<html lang="en">
<head>
<meta charset="utf-8">
<title>Bright Valley Centre – Business Card</title>
<link rel="stylesheet" href="https://fonts.googleapis.com/css2?family=Open+Sans:wght@300;400;600&family=Roboto+Slab:wght@400&display=swap">
<style>
  :root {
    --bg: #d9dadc;
    --sky: #1fb4ee;
    --sky-light: #7fd6fa;
    --sky-pale: #d8f3fe;
    --sky-band: #6fcdf6;
    --sky-deep: #1a8fe0;
    --white: #ffffff;
    --ink: #4a4a4a;
    --ink-soft: #6d6d6d;
    --rule: #d2d2d2;
  }
  * { box-sizing: border-box; margin: 0; padding: 0; }
  html, body { width: 1200px; height: 800px; overflow: hidden; }
  body {
    background: var(--bg);
    font-family: "Open Sans", Arial, sans-serif;
    display: flex;
    align-items: center;
    justify-content: center;
    gap: 80px;
  }
  .card {
    width: 320px;
    height: 540px;
    position: relative;
    overflow: hidden;
    box-shadow: 0 10px 30px rgba(0,0,0,0.12);
  }

  /* Front */
  .card--front {
    background: radial-gradient(circle at 50% 42%, var(--sky-pale) 0%, var(--sky-light) 35%, var(--sky) 75%);
    display: flex;
    flex-direction: column;
    align-items: center;
    justify-content: center;
    color: var(--white);
  }
  .brand {
    display: flex;
    align-items: center;
    gap: 14px;
    margin-top: 20px;
  }
  .brand__dot {
    width: 22px; height: 22px;
    border-radius: 50%;
    background: var(--white);
    flex: none;
  }
  .brand__name {
    font-weight: 600;
    font-size: 24px;
    line-height: 1.15;
    letter-spacing: 1px;
    text-transform: uppercase;
    color: var(--white);
  }
  .tagline {
    margin-top: 70px;
    font-size: 17px;
    font-weight: 400;
    letter-spacing: 0.5px;
    text-transform: uppercase;
  }

  /* Back */
  .card--back {
    background: var(--white);
    border-top: 6px solid var(--sky-deep);
    display: flex;
    flex-direction: column;
  }
  .profile {
    flex: 0 0 255px;
    padding: 62px 34px 0;
  }
  .profile__name {
    font-family: "Roboto Slab", Georgia, serif;
    font-size: 36px;
    font-weight: 400;
    color: var(--ink);
    line-height: 1;
  }
  .profile__name .first { color: var(--sky); }
  .profile__creds {
    margin-top: 12px;
    font-size: 10.5px;
    color: var(--ink-soft);
    letter-spacing: 0.4px;
    text-transform: uppercase;
    padding-left: 52px;
  }
  .profile__rule {
    margin: 18px 0 14px 52px;
    width: 160px;
    border: 0;
    border-top: 1px solid var(--rule);
  }
  .profile__role {
    padding-left: 52px;
    font-size: 10.5px;
    line-height: 1.6;
    color: var(--ink-soft);
    letter-spacing: 0.4px;
    text-transform: uppercase;
  }
  .contact {
    flex: 1;
    background: var(--sky-band);
    border-bottom: 14px solid var(--sky-deep);
    padding: 30px 30px 0;
    color: var(--white);
    list-style: none;
    display: flex;
    flex-direction: column;
    gap: 22px;
  }
  .contact__item {
    display: flex;
    align-items: center;
    gap: 14px;
    font-size: 12.5px;
    line-height: 1.35;
  }
  .contact__icon {
    width: 30px; height: 30px;
    flex: none;
  }
</style>
</head>
<body>

  <section class="card card--front" aria-label="Card front">
    <div class="brand">
      <span class="brand__dot"></span>
      <span class="brand__name">Bright<br>Valley<br>Centre</span>
    </div>
    <p class="tagline">Experts in Hearing Care</p>
  </section>

  <section class="card card--back" aria-label="Card back">
    <header class="profile">
      <h1 class="profile__name"><span class="first">Dr Arjun</span> Mehta</h1>
      <p class="profile__creds">Aud. MASLP. MAUDSA.CCP</p>
      <hr class="profile__rule">
      <p class="profile__role">Chief Audiologist &amp;<br>Speech Language Pathologist</p>
    </header>

    <ul class="contact">
      <li class="contact__item">
        <svg class="contact__icon" viewBox="0 0 30 30" aria-hidden="true">
          <circle cx="15" cy="15" r="13.5" fill="none" stroke="#fff" stroke-width="1.6"/>
          <path d="M15 7.5a5 5 0 0 0-5 5c0 3.8 5 9.5 5 9.5s5-5.7 5-9.5a5 5 0 0 0-5-5z" fill="#fff"/>
          <circle cx="15" cy="12.5" r="1.9" fill="var(--sky-band)"/>
        </svg>
        <span>F4 Lotus Arcade, Ravipeth,<br>Dharwad - 580 041. (Karnataka) India</span>
      </li>
      <li class="contact__item">
        <svg class="contact__icon" viewBox="0 0 30 30" aria-hidden="true">
          <circle cx="15" cy="15" r="13.5" fill="none" stroke="#fff" stroke-width="1.6"/>
          <path d="M11.2 8.5l2 3.3-1.4 1.6c.8 1.8 2.1 3.1 3.9 3.9l1.6-1.4 3.3 2-.9 2.8c-5.8-.2-10.4-4.8-10.6-10.6z" fill="#fff"/>
        </svg>
        <span>9845106372<br>0836 2470518</span>
      </li>
      <li class="contact__item">
        <svg class="contact__icon" viewBox="0 0 30 30" aria-hidden="true">
          <circle cx="15" cy="15" r="13.5" fill="none" stroke="#fff" stroke-width="1.6"/>
          <circle cx="15" cy="15" r="7" fill="none" stroke="#fff" stroke-width="1.4"/>
          <ellipse cx="15" cy="15" rx="3" ry="7" fill="none" stroke="#fff" stroke-width="1.2"/>
          <line x1="8" y1="15" x2="22" y2="15" stroke="#fff" stroke-width="1.2"/>
        </svg>
        <span>arjunmehta@mailbox.in<br>www.brightvalleycentre.in</span>
      </li>
    </ul>
  </section>

</body>
</html>
```